Porch Light Podcast Cover Graphic

We need a graphic designed for a new podcast called "Porch Light." The graphic will be used on multiple podcasting platforms as the lead graphic advertising the podcast. The podcast consists of interviews of individuals sharing their life experiences including challenges, successes, lessons learned, and unexpected turns. The purpose of the podcast is to help listeners and participants learn from the life experiences of everyday neighbors. This podcast has a heavy Christian foundation on the parable of the good samaritan. We believe that through hearing the experiences of everyday neighbors, listeners can be strengthened, nourished, and aided to handle their own life challenges and trials. We would like the final design to be simple and reflective of the purpose and the parable of the good samaritan. The final design needs to have the title of the podcast, "Porch Light." We believe the best designs will limit the number of colors to less than 5 and will look good in a monochromatic version as well as a color version. We think the color white should be the main color. The graphic should be square in dimensions. We have considered having two hands grasping each other as if to lift the hand from below, but open to other creative simple takes to convey the lessons from the good samaritan.

```html
<!DOCTYPE html>
<html lang="en">
<head>
<meta charset="UTF-8">
<title>Porch Light — Podcast Cover</title>
<link href="https://fonts.googleapis.com/css2?family=Oswald:wght@700&family=Yellowtail&display=swap" rel="stylesheet">
<style>
  :root {
    --stage: #3a3a3a;
    --paper: #ffffff;
    --paper-shade: #eef2f4;
    --frame-line: #2e3236;
    --skyline-light: #e6e8ea;
    --skyline-dark: #a9adb1;
    --hands-light: #c9c3b4;
    --hands-dark: #7d7665;
    --blue-light: #a6dcf5;
    --blue-mid: #4b97c9;
    --blue-dark: #124f86;
  }
  html, body {
    margin: 0;
    padding: 0;
    width: 767px;
    height: 1200px;
    overflow: hidden;
    background: var(--stage);
  }
  .cover {
    position: absolute;
    left: 0;
    top: 216px;
    width: 767px;
    height: 767px;
    overflow: hidden;
    background: linear-gradient(180deg, var(--paper) 0%, var(--paper-shade) 55%, var(--paper) 100%);
  }
  .cover__art {
    position: absolute;
    inset: 0;
  }
  .cover__script {
    position: absolute;
    left: 150px;
    top: 420px;
    margin: 0;
    font-family: "Yellowtail", cursive;
    font-weight: 400;
    font-size: 170px;
    line-height: 1;
    transform: rotate(-8deg);
    background: linear-gradient(200deg, var(--blue-light) 0%, var(--blue-mid) 45%, var(--blue-dark) 100%);
    -webkit-background-clip: text;
    background-clip: text;
    color: transparent;
    z-index: 3;
  }
  .cover__title {
    position: absolute;
    left: 0;
    right: 0;
    top: 560px;
    margin: 0;
    text-align: center;
    font-family: "Oswald", sans-serif;
    font-weight: 700;
    font-size: 186px;
    line-height: 1;
    letter-spacing: 2px;
    background: linear-gradient(180deg, var(--blue-light) 18%, var(--blue-mid) 55%, var(--blue-dark) 92%);
    -webkit-background-clip: text;
    background-clip: text;
    color: transparent;
    z-index: 2;
  }
</style>
</head>
<body>
  <main class="cover">
    <svg class="cover__art" width="767" height="767" viewBox="0 0 767 767">
      <defs>
        <linearGradient id="skyline-tone" x1="0" y1="0" x2="0" y2="1">
          <stop offset="0" stop-color="var(--skyline-dark)" stop-opacity="0.55"/>
          <stop offset="1" stop-color="var(--skyline-light)" stop-opacity="0"/>
        </linearGradient>
        <linearGradient id="hands-tone" x1="0" y1="0" x2="1" y2="1">
          <stop offset="0" stop-color="var(--hands-light)"/>
          <stop offset="0.6" stop-color="var(--hands-dark)"/>
          <stop offset="1" stop-color="var(--hands-light)"/>
        </linearGradient>
      </defs>

      <rect class="skyline" role="img" aria-label="Grey city skyline of high-rise buildings"
            x="0" y="100" width="767" height="420" fill="url(#skyline-tone)"/>

      <g class="frame-lines" fill="none" stroke="var(--frame-line)" stroke-width="2.5">
        <polyline points="186,31 664,31 664,180"/>
        <polyline points="202,46 686,46 686,250"/>
        <polyline points="218,62 708,62 708,413"/>
      </g>

      <polygon class="helping-hands" role="img"
               aria-label="Sepia photo of one hand firmly grasping another by the wrist to lift it up"
               points="0,0 210,0 451,97 701,266 767,347 767,621 661,596 484,484 242,266 0,193"
               fill="url(#hands-tone)"/>
    </svg>

    <p class="cover__script">Porch</p>
    <h1 class="cover__title">LIGHT</h1>
  </main>
</body>
</html>
```